Very clean, very simple business card needed.

I am looking for a VERY simple business card. I have attached our logo. I would like it to be a mainly white card. I have picked double sided but would be open to single as well. I want the overall feel to be simple, classic, and professional. Thank you.

Industry/Entity Type

Consultant

Contact Information for Business Card

Daniel Fenwick

2870 North 9th Avenue, Summit Floor, Larkmoor, Ashvale 60871
dan@belmorevista.com
www.belmorevista.com

Font styles to use
Serif

Colors

Designer to choose colors to be used in the design.

Requirements
Must have
• The business card details and in an editable form to change the names and emails of employees easily.
Nice to have
• n/a
Should not have
• Pictures, big lines and stripes, too much color.

```html
<!DOCTYPE html>
<html lang="en">
<head>
<meta charset="utf-8">
<title>Belmore Vista – Business Card</title>
<link rel="stylesheet" href="https://fonts.googleapis.com/css2?family=Source+Sans+3:wght@300;400;600;700&display=swap">
<style>
  :root {
    --backdrop: #232325;
    --paper: #ffffff;
    --navy: #2c2a74;
    --navy-ink: #2e2b6f;
    --on-navy: #ffffff;
    --on-navy-soft: #e4e3f2;
  }
  * { box-sizing: border-box; margin: 0; padding: 0; }
  html, body {
    width: 1200px; height: 900px; overflow: hidden;
    background: var(--backdrop);
    font-family: "Source Sans 3", "Helvetica Neue", Arial, sans-serif;
  }
  .sheet {
    width: 1200px; height: 900px;
    display: flex; flex-direction: column;
    align-items: center; justify-content: center; gap: 34px;
  }
  .card {
    width: 700px; height: 400px;
    position: relative;
    box-shadow: 0 10px 30px rgba(0,0,0,.45);
  }

  /* Front: white contact side */
  .card--front { background: var(--paper); color: var(--navy-ink); }
  .brand {
    position: absolute; left: 44px; top: 40px;
    display: flex; align-items: flex-end; gap: 16px;
  }
  .brand__square {
    width: 40px; height: 40px; background: var(--navy);
  }
  .brand__name {
    font-size: 30px; font-weight: 400; letter-spacing: 3px; line-height: 1;
    text-transform: uppercase; color: var(--navy-ink);
  }
  .contact {
    position: absolute; left: 44px; top: 130px;
    font-size: 16px; line-height: 1.45; color: var(--navy-ink);
  }
  .contact__name { font-weight: 700; font-size: 16px; margin-bottom: 16px; }
  .contact__line { font-weight: 400; }

  /* Back: navy brand side */
  .card--back {
    background: var(--navy); color: var(--on-navy);
    display: flex; flex-direction: column; align-items: center; justify-content: center;
    text-align: center;
  }
  .back-mark {
    width: 54px; height: 54px; border: 2px solid var(--on-navy);
    margin-bottom: 18px;
  }
  .back-brand {
    font-size: 30px; font-weight: 400; letter-spacing: 3px;
    text-transform: uppercase; color: var(--on-navy);
    margin-bottom: 14px;
  }
  .tagline {
    font-size: 24px; font-weight: 300; line-height: 1.2;
    color: var(--on-navy-soft);
  }
</style>
</head>
<body>
  <main class="sheet">
    <section class="card card--front" aria-label="Business card front">
      <div class="brand">
        <span class="brand__square"></span>
        <span class="brand__name">Belmore Vista</span>
      </div>
      <div class="contact">
        <p class="contact__name">Daniel Fenwick</p>
        <p class="contact__line">2870 North 9th Avenue, Summit Floor, Larkmoor, Ashvale 60871</p>
        <p class="contact__line">dan@belmorevista.com</p>
        <p class="contact__line">www.belmorevista.com</p>
      </div>
    </section>

    <section class="card card--back" aria-label="Business card back">
      <span class="back-mark"></span>
      <p class="back-brand">Belmore Vista</p>
      <p class="tagline">Building Lasting Trade Partnerships In<br>The Western Markets</p>
    </section>
  </main>
</body>
</html>
```